Business card design for Velluto Events, and Event & Entertainment business

The business card design is for a new business venture, Velluto Events. This company offers Event management, entertainment management and also Latin dance tuition. We currently run Latin dance festivals in Australia & also teach street Latin. This business card is for the director, Mara Dunhill. The Logo has already been designed. So, I need the new design to incorporate and go with the existing Logo.

The look I like is clean, simple & elegant but I also want it to be sexy. Elegant, but not corporate. Clean & simple but not boring :-)

If you want to add another design element as well as using the Logo, please use something with movement. I like ripples or swirls for example.

I would also like to have part of the card embossed or Spot UV pressed so I would like some part of the design to have texture.

Text for the Cards is as follows;

Velluto Events ( Logo attached )

Mara Dunhill

EVENTS & ENTERTAINMENT MANAGEMENT

m: 0478 352 601
e: mara@vellutoevents.com.au
f Velluto Events

www.vellutoevents.com.au

Please try portrait layout.

Thanks, Mara
Updates

Hello Designers, Thank you to all of you who have submitted designs for Velluto Events. I will make up my mind now from what I have already been sent. Very close to making a decision :-) Thank you, Mara

Target Market(s)

Adults, 18 - 60 age group. People who are active. People interested in different cultures. People who like to travel. Please who like to have fun. People who are passionate about Latin dance.

Industry/Entity Type

Entertainment

Font styles to use
Sans Serif
Script

Colors
9bcb3c
ec1f27
ffffff

Requirements
Must have
• Logo + All text listed in brief
Nice to have
• An extra design feature or background image that could be embossed or spot uv pressed to add texture & flare.

```html
<!DOCTYPE html>
<html lang="en">
<head>
<meta charset="utf-8">
<title>Velluto Events – Business Card</title>
<link rel="stylesheet" href="https://fonts.googleapis.com/css2?family=Open+Sans:wght@400;600;700&display=swap">
<style>
  :root {
    --crimson: #c8213f;
    --crimson-deep: #a3162f;
    --leaf: #9bcb3c;
    --paper: #ffffff;
    --ink: #3a3a3a;
    --ink-soft: #6b6b6b;
    --backdrop: #ebe8e5;
    --card-w: 520px;
    --card-h: 300px;
  }
  * { box-sizing: border-box; margin: 0; padding: 0; }
  html, body {
    width: 1200px; height: 800px; overflow: hidden;
    background: var(--backdrop);
    font-family: "Open Sans", Arial, sans-serif;
  }
  .stage { position: relative; width: 1200px; height: 800px; }
  .card {
    position: absolute; top: 250px;
    width: var(--card-w); height: var(--card-h);
    border-radius: 18px; overflow: hidden;
    box-shadow: 0 10px 28px rgba(0,0,0,.18);
  }

  /* Back of card */
  .card--back {
    left: 60px;
    background: linear-gradient(135deg, #d22c4c 0%, var(--crimson) 45%, var(--crimson-deep) 100%);
    color: var(--paper);
  }
  .card--back .brand {
    position: absolute; left: 0; right: 0; top: 112px;
    display: flex; align-items: center; justify-content: center; gap: 12px;
  }
  .card--back .brand-dot { width: 14px; height: 14px; border-radius: 50%; background: var(--paper); }
  .card--back .brand-name { font-size: 34px; font-weight: 600; color: var(--paper); letter-spacing: .5px; }
  .card--back .web {
    position: absolute; left: 0; right: 0; bottom: 22px;
    text-align: center; font-size: 13px; letter-spacing: .5px;
  }

  /* Front of card */
  .card--front { left: 620px; background: var(--paper); }
  .card--front .wave { position: absolute; inset: 0; }
  .card--front .brand {
    position: absolute; right: 40px; top: 28px;
    display: flex; align-items: center; gap: 10px;
  }
  .card--front .brand-dot { width: 12px; height: 12px; border-radius: 50%; background: var(--crimson); }
  .card--front .brand-name { font-size: 30px; font-weight: 600; color: var(--ink); }
  .card--front .tagline {
    position: absolute; right: 30px; top: 78px;
    font-size: 10.5px; letter-spacing: 2.4px; color: var(--ink-soft);
  }
  .contacts {
    position: absolute; left: 18px; top: 116px;
    list-style: none; color: var(--paper); font-size: 12px;
  }
  .contacts li { display: flex; align-items: center; gap: 7px; margin-bottom: 6px; white-space: nowrap; }
  .contact-icon {
    width: 13px; height: 13px; border-radius: 2px; background: var(--leaf);
    display: inline-flex; align-items: center; justify-content: center; flex: none;
  }
  .person { position: absolute; right: 34px; top: 170px; text-align: right; }
  .person-name { font-size: 20px; font-weight: 700; color: var(--crimson); letter-spacing: .5px; }
  .person-role { font-size: 12px; font-weight: 600; color: var(--ink); }
  .card--front .web {
    position: absolute; right: 30px; bottom: 10px;
    color: var(--paper); font-size: 13px; letter-spacing: .3px;
  }
</style>
</head>
<body>
<main class="stage">

  <section class="card card--back" aria-label="Card back">
    <div class="brand">
      <span class="brand-dot"></span>
      <span class="brand-name">Velluto Events</span>
    </div>
    <p class="web">www.vellutoevents.com.au</p>
  </section>

  <section class="card card--front" aria-label="Card front">
    <svg class="wave" viewBox="0 0 520 300" preserveAspectRatio="none" aria-hidden="true">
      <defs>
        <linearGradient id="wave-fill" x1="0" y1="0" x2="1" y2="1">
          <stop offset="0" stop-color="#d22c4c"/>
          <stop offset="1" stop-color="#a3162f"/>
        </linearGradient>
      </defs>
      <path d="M0,100 C100,94 200,98 245,135 C285,175 320,222 420,240 C470,249 500,252 520,254 L520,300 L0,300 Z" fill="url(#wave-fill)"/>
    </svg>

    <div class="brand">
      <span class="brand-dot"></span>
      <span class="brand-name">Velluto Events</span>
    </div>
    <p class="tagline">EVENTS &amp; ENTERTAINMENT MANAGEMENT</p>

    <ul class="contacts">
      <li>
        <span class="contact-icon">
          <svg width="9" height="9" viewBox="0 0 24 24" aria-hidden="true"><path fill="#fff" d="M6.6 10.8a15.1 15.1 0 0 0 6.6 6.6l2.2-2.2c.3-.3.7-.4 1-.2 1.1.4 2.3.6 3.6.6.6 0 1 .4 1 1V20c0 .6-.4 1-1 1C10.6 21 3 13.4 3 4c0-.6.4-1 1-1h3.5c.6 0 1 .4 1 1 0 1.3.2 2.5.6 3.6.1.3 0 .7-.2 1z"/></svg>
        </span>0478 352 601
      </li>
      <li>
        <span class="contact-icon">
          <svg width="9" height="9" viewBox="0 0 24 24" aria-hidden="true"><path fill="#fff" d="M2 5h20v14H2z M2 5l10 8 10-8" stroke="#9bcb3c" stroke-width="2"/></svg>
        </span>mara@vellutoevents.com.au
      </li>
      <li><span class="contact-icon"></span>Velluto Events</li>
    </ul>

    <div class="person">
      <p class="person-name">MARA DUNHILL</p>
      <p class="person-role">Director</p>
    </div>

    <p class="web">www.vellutoevents.com.au</p>
  </section>

</main>
</body>
</html>
```